Startup online payment business - Sporting / Golf, Swift Tee payment

Background:
Our business name is "Swift Tee" we provide online payments for golfing services via our website. We currently have a logo used on our website. No other design style has been developed. Our aim is to remove cash payments for service at golf clubs.

Our Key Values:
Quick and easy
Formal and polite
Fun with professional boundary
Mate-ship relationships
100% online digital

What we want from you:
Marketing design to be used on posters and stickers in a retail setting to direct customers to our online payment Chanel.
Design must incorporate attached logo, URL swifttee.com.au and our key values can act as a guide the type of design. We have used color Hex#007672 for logo background. We are open to use other colors.

Target Market(s)

Golf clubs and golf players

Industry/Entity Type

Golf Course

Font styles to use
Sans Serif

Requirements
Must have
• Directions to online payment via URL: swifttee.com.au
Nice to have
• We like the idea of the slogan: No Cash - No worries. Have attached home screen that will be available from URL link. Consideration if using mobile phone in image. Push the online payment and steps 1. Visit swifttee.com 2. Select club 3. Confirm payment
Should not have
• Cartoons

```html
<!DOCTYPE html>
<html lang="en">
<head>
<meta charset="utf-8">
<title>Swift Tee – Welcome Flyer</title>
<link href="https://fonts.googleapis.com/css2?family=Montserrat:wght@300;400;500;600;700&display=swap" rel="stylesheet">
<style>
  :root {
    --teal: #13877f;
    --teal-deep: #0f7770;
    --teal-light: #2fa395;
    --teal-mist: #3aa89a;
    --white: #ffffff;
    --ink: #1d1d1d;
    --page: #ecebe7;
    --rule: #9a9a9a;
  }
  * { margin: 0; padding: 0; box-sizing: border-box; }
  html, body { width: 1200px; height: 1200px; overflow: hidden; }
  body {
    background: var(--page);
    font-family: "Montserrat", sans-serif;
    color: var(--ink);
  }
  .flyer {
    position: absolute;
    left: 194px; top: 30px;
    width: 812px; height: 1140px;
    background: var(--white);
    overflow: hidden;
    box-shadow: 0 6px 24px rgba(0,0,0,.18);
  }
  .hero-photo {
    position: absolute; left: 0; top: 0; width: 812px; height: 800px;
    background:
      radial-gradient(ellipse at 50% 20%, rgba(58,168,154,.55), transparent 60%),
      linear-gradient(180deg, #1f9589 0%, #168a80 45%, #13857c 100%);
  }
  .hero-wave { position: absolute; left: 0; top: 520px; width: 812px; height: 300px; }
  .brand-name {
    position: absolute; top: 92px; left: 0; width: 100%;
    text-align: center; color: var(--white);
    font-weight: 600; font-size: 66px; letter-spacing: 3px;
  }
  .welcome-kicker {
    position: absolute; top: 270px; left: 0; width: 100%;
    text-align: center; color: var(--white);
    font-weight: 500; font-size: 17px; letter-spacing: 16px; padding-left: 16px;
  }
  .welcome-title {
    position: absolute; top: 292px; left: 0; width: 100%;
    text-align: center; color: var(--white);
    font-weight: 700; font-size: 58px; letter-spacing: 0.5px;
  }
  .welcome-lede {
    position: absolute; top: 376px; left: 40px; width: 732px;
    text-align: center; color: var(--white);
    font-weight: 400; font-size: 22px; line-height: 29px;
  }
  .intro {
    position: absolute; left: 36px; top: 614px; width: 620px;
    font-size: 15.5px; line-height: 19px; font-weight: 400;
  }
  .intro p + p { margin-top: 19px; }
  .values-label {
    position: absolute; left: 262px; top: 790px; width: 245px; height: 42px;
    background: var(--teal-deep); color: var(--white);
    border-radius: 21px; text-align: center;
    font-weight: 700; font-size: 25px; line-height: 42px;
  }
  .values {
    position: absolute; left: 0; top: 868px; width: 812px; height: 140px;
  }
  .value {
    position: absolute; top: 0; width: 150px; margin-left: -75px;
    text-align: center; font-size: 16px; line-height: 19px;
  }
  .value svg { display: block; margin: 0 auto 16px; width: 60px; height: 64px; fill: var(--teal-deep); }
  .value-divider {
    position: absolute; top: 26px; height: 106px;
    border-left: 1px dotted var(--rule);
  }
  .footer-shadow {
    position: absolute; left: 60px; top: 1034px; width: 692px; height: 6px;
    background: radial-gradient(ellipse at center, rgba(0,0,0,.14), transparent 70%);
  }
  .footer {
    position: absolute; left: 0; bottom: 0; width: 812px; height: 73px;
    background: var(--teal-light); color: var(--white);
    text-align: center; font-size: 20px; line-height: 73px; font-weight: 400;
  }
  .footer strong { font-weight: 700; }
</style>
</head>
<body>
<main class="flyer">
  <div class="hero-photo" role="img" aria-label="Faded photo of golfers on a course with a golf bag, tinted teal"></div>
  <svg class="hero-wave" viewBox="0 0 812 300" preserveAspectRatio="none" aria-hidden="true">
    <path d="M0 40 C 200 0, 420 -10, 600 60 C 700 100, 770 160, 812 215 L812 300 L0 300 Z" fill="var(--teal-mist)"/>
    <path d="M0 53 C 200 15, 420 10, 600 80 C 700 120, 770 190, 812 257 L812 300 L0 300 Z" fill="var(--white)"/>
  </svg>

  <div class="brand-name">SWIFT TEE</div>
  <div class="welcome-kicker">WELCOME</div>
  <h1 class="welcome-title">TO SWIFT TEE</h1>
  <p class="welcome-lede">Swift Tee is here to<br>support Golf Clubs embrace new strategies for success in a<br>rapidly changing world.</p>

  <section class="intro">
    <p>Moving toward a future cashless society, Swift Tee are<br>developing new mobile payment methods in order for Clubs to<br>cater for the next generation of players and community expectations.</p>
    <p>Interested in learning more about how we can help grow your Clubs earning potential?</p>
  </section>

  <div class="values-label">Our Key Values:</div>

  <section class="values">
    <div class="value" style="left:78px">
      <svg viewBox="0 0 60 64" aria-hidden="true">
        <path d="M22 28 l10-10 a4 4 0 0 1 6 6 l-6 6 h10 a4 4 0 0 1 0 8 h-2 a4 4 0 0 1 0 8 h-2 a4 4 0 0 1 -1 8 H26 a12 12 0 0 1 -12 -12 v-8 a6 6 0 0 1 8 -6 z" fill="none" stroke="var(--teal-deep)" stroke-width="4" stroke-linejoin="round"/>
        <rect x="24" y="2" width="3" height="10" rx="1.5"/>
        <rect x="34" y="4" width="3" height="9" rx="1.5" transform="rotate(30 35 8)"/>
        <rect x="13" y="6" width="3" height="9" rx="1.5" transform="rotate(-35 14 10)"/>
      </svg>
      Quick<br>and easy
    </div>
    <div class="value-divider" style="left:139px"></div>
    <div class="value" style="left:217px">
      <svg viewBox="0 0 60 64" aria-hidden="true">
        <circle cx="30" cy="8" r="7"/>
        <path d="M22 18 h16 a3 3 0 0 1 3 3 v20 h-4 v21 h-5 v-21 h-4 v21 h-5 v-21 h-4 v-20 a3 3 0 0 1 3 -3 z"/>
      </svg>
      Formal<br>and polite
    </div>
    <div class="value-divider" style="left:294px"></div>
    <div class="value" style="left:374px">
      <svg viewBox="0 0 60 64" aria-hidden="true">
        <circle cx="30" cy="4" r="4"/><circle cx="17" cy="8" r="4"/><circle cx="43" cy="8" r="4"/>
        <circle cx="7" cy="20" r="4"/><circle cx="53" cy="20" r="4"/>
        <circle cx="30" cy="26" r="7"/>
        <path d="M4 34 l8-6 l10 10 h16 l10-10 l8 6 l-14 14 v14 h-24 v-14 z"/>
      </svg>
      Fun with<br>professional<br>boundary
    </div>
    <div class="value-divider" style="left:459px"></div>
    <div class="value" style="left:546px">
      <svg viewBox="0 0 60 64" aria-hidden="true">
        <path d="M30 60 L6 36 A14 14 0 0 1 30 14 A14 14 0 0 1 54 36 Z"/>
        <path d="M16 36 l10-8 h10 l8 8 l-10 10 l-4-4 l-4 4 z" fill="var(--white)"/>
      </svg>
      Mate-ship<br>relationships
    </div>
    <div class="value-divider" style="left:632px"></div>
    <div class="value" style="left:709px">
      <svg viewBox="0 0 60 64" aria-hidden="true">
        <rect x="14" y="8" width="30" height="18" rx="2" fill="none" stroke="var(--teal-deep)" stroke-width="3"/>
        <rect x="6" y="22" width="46" height="36" rx="4"/>
        <rect x="38" y="34" width="18" height="12" rx="3" fill="var(--white)"/>
        <circle cx="44" cy="40" r="2.5"/>
      </svg>
      100%<br>online digital
    </div>
  </section>

  <div class="footer-shadow"></div>
  <footer class="footer">visit our website for more info <strong>www.swifttee.com.au</strong></footer>
</main>
</body>
</html>
```